Restaurant needs a vertical banner for fried catfish

Our restaurant is looking for an eye-catching 78.75in. x 36in. vertical physical banner ad for our fried catfish. Photos for the fried catfish will be provided as a reference but we will also accept anything similar to the photo. We will be using the following as our receptacle: https://www.plankoria.example/banner-stand/retractable-banner-stands/
The design must incorporate the following flavor texts:
Fried Catfish
Always Fresh!
Made from Scratch
Hand-cut Fillets
The Best Catfish in Texas
Served with fries, hush puppies, and a 32oz fountain drink
Also available by the pound!
The final design should be creative, professional, and eye-catching for customers.
Updates
Colors
Designer to choose colors to be used in the design.
Requirements
Must have
- We are open to any and all design elements, albeit the 'flavor texts' should not overpower, but complement the fried catfish photo. 'Fried Catfish' can be used in lieu of a main title/logo.
Nice to have
- Transparent or textured backgrounds that can encompass any or all part of the banner such as a cutting board, shadows, abstract, etc to show depth are a plus.
- Use of vectors or objects such as ribbons or shapes to encapsulate the 'flavor texts' are also encouraged.

```html
<!DOCTYPE html>
<html lang="en">
<head>
<meta charset="utf-8">
<title>Fried Catfish Vertical Banner</title>
<link rel="stylesheet" href="https://fonts.googleapis.com/css2?family=Lobster&family=Montserrat:wght@500;600&display=swap">
<style>
  :root {
    --green: #07964a;
    --yellow: #fedf19;
    --white: #ffffff;
    --backdrop: #e9eaec;
    --photo-warm: #b7833f;
    --photo-deep: #6f4a22;
    --photo-light: #e6d3ad;
  }
  * { box-sizing: border-box; margin: 0; padding: 0; }
  html, body {
    width: 1200px;
    height: 1067px;
    overflow: hidden;
    background: var(--backdrop);
  }
  .banner {
    position: absolute;
    left: 357px;
    top: 23px;
    width: 485px;
    height: 1020px;
    background: var(--yellow);
    overflow: hidden;
    font-family: "Montserrat", Arial, sans-serif;
  }
  .banner > * { position: absolute; left: 0; width: 485px; }
  .headline {
    top: 0;
    height: 99px;
    display: flex;
    align-items: center;
    justify-content: center;
    font-family: "Lobster", cursive;
    font-weight: 400;
    font-size: 50px;
    color: var(--green);
    padding-top: 6px;
  }
  .title-band { top: 99px; height: 102px; background: var(--green); }
  .photo {
    background:
      radial-gradient(ellipse 55% 40% at 50% 55%, var(--photo-warm), transparent 75%),
      linear-gradient(160deg, var(--photo-light), var(--photo-deep));
  }
  .photo-plate { top: 201px; height: 283px; }
  .photo-platter { top: 594px; height: 235px; }
  .title-mark {
    left: 156px;
    top: 112px;
    width: 172px;
    height: 172px;
    border-radius: 50%;
    background: var(--white);
    display: flex;
    align-items: center;
    justify-content: center;
    text-align: center;
    color: var(--green);
    font-weight: 600;
    font-size: 25px;
    line-height: 1.15;
    letter-spacing: 1px;
  }
  .features { top: 484px; height: 110px; background: var(--white); }
  .ribbon {
    position: absolute;
    height: 31px;
    display: flex;
    align-items: center;
    justify-content: center;
    font-weight: 600;
  }
  .ribbon--green { left: 108px; width: 269px; background: var(--green); color: var(--white); font-size: 16px; }
  .ribbon--yellow { left: 5px; width: 475px; background: var(--yellow); color: var(--green); font-size: 21px; }
  .ribbon--top { top: 8px; }
  .ribbon--mid { top: 40px; }
  .ribbon--bottom { top: 72px; }
  .pound-tag {
    left: 180px;
    top: 751px;
    width: 124px;
    height: 78px;
    background: var(--yellow);
    border-radius: 62px 62px 0 0;
    display: flex;
    flex-direction: column;
    align-items: center;
    justify-content: flex-end;
    padding-bottom: 8px;
    color: var(--green);
    font-weight: 600;
    font-size: 13px;
    line-height: 1.35;
    text-align: center;
  }
  .serving { top: 829px; height: 191px; }
  .serving svg { position: absolute; left: 0; top: 0; }
  .serving-text {
    position: absolute;
    left: 0;
    top: 26px;
    width: 485px;
    text-align: center;
    color: var(--white);
    font-weight: 600;
    font-size: 22px;
    line-height: 29px;
  }
</style>
</head>
<body>
  <main class="banner">
    <h1 class="headline">Always Fresh!</h1>
    <div class="title-band"></div>
    <div class="photo photo-plate" role="img" aria-label="Photo of fried catfish fillets with fries, hush puppies and tartar sauce on a white plate, tomatoes and onions behind"></div>

    <p class="title-mark">FRIED<br>CATFISH</p>

    <section class="features">
      <p class="ribbon ribbon--green ribbon--top">Made from Scratch</p>
      <p class="ribbon ribbon--yellow ribbon--mid">The Best Catfish in Texas</p>
      <p class="ribbon ribbon--green ribbon--bottom">Hand-cut Fillets</p>
    </section>

    <div class="photo photo-platter" role="img" aria-label="Photo of golden fried catfish fillets on a plate with hush puppy and sauce, lemons, tomatoes and onions behind"></div>

    <p class="pound-tag">Also available<br>by the pound!</p>

    <section class="serving">
      <svg width="485" height="191" viewBox="0 0 485 191" aria-hidden="true">
        <path d="M0,0 H485 V95 Q242.5,215 0,95 Z" fill="var(--green)"/>
      </svg>
      <p class="serving-text">Served with fries,<br>hush puppies, &amp;<br>a 32oz fountain drink</p>
    </section>
  </main>
</body>
</html>
```